Real Estate Development Company Stationary

We need our company, business card, letterhead, pocket folder and envelope designed.

We are a new real estate development company. We focus on data centre, commercial and real estate development.

Please see attached for our logo. Since it's a new logo, you still can make minor adjust if you like it makes senses

The client has sent me a business card he really likes. Please see file 3.

Target Market(s)

Real Estate Investors
Large corporations
Home buyers

Industry/Entity Type

Real Estate

```html
<!DOCTYPE html>
<html lang="en">
<head>
<meta charset="utf-8">
<title>Verano Development Inc. — Stationery</title>
<link rel="stylesheet" href="https://fonts.googleapis.com/css2?family=Mulish:wght@400;600&family=Montserrat:wght@600&display=swap">
<style>
  :root {
    --stage: #000000;
    --paper: #ffffff;
    --brand-blue: #0b4686;
    --brand-teal: #2a7a7a;
    --brand-green: #77bf43;
    --ink: #4a4a4a;
    --label: #ffffff;
    --ghost-blue: rgba(60, 70, 170, 0.12);
    --band: linear-gradient(90deg, var(--brand-blue) 0%, var(--brand-teal) 45%, var(--brand-green) 100%);
  }
  html, body {
    margin: 0;
    padding: 0;
    width: 1200px;
    height: 986px;
    overflow: hidden;
    background: var(--stage);
    font-family: "Mulish", "Century Gothic", sans-serif;
  }
  .stage { position: relative; width: 1200px; height: 986px; }

  .sheet { position: absolute; background: var(--paper); overflow: hidden; }
  .band { position: absolute; left: 0; right: 0; bottom: 0; background: var(--band); }
  .ghost-mark { position: absolute; }

  .wordmark {
    position: absolute;
    display: flex;
    align-items: center;
    color: var(--brand-green);
    font-weight: 600;
    white-space: nowrap;
    line-height: 1;
  }
  .wordmark .dot { border-radius: 50%; background: var(--brand-blue); margin-right: 0.3em; flex: none; }

  .address { position: absolute; color: var(--ink); margin: 0; white-space: nowrap; }

  /* Letterhead */
  .letterhead { left: 63px; top: 45px; width: 674px; height: 872px; }
  .letterhead .band { height: 44px; }
  .letterhead .wordmark { left: 510px; top: 50px; font-size: 30px; }
  .letterhead .wordmark .dot { width: 30px; height: 30px; }
  .letterhead .address { left: 510px; top: 98px; font-size: 11.5px; line-height: 15.4px; }
  .letterhead .ghost-mark { left: -80px; top: 420px; width: 400px; height: 400px; }

  /* Envelope */
  .envelope { left: 506px; top: 244px; width: 662px; height: 332px; }
  .envelope .band { height: 34px; }
  .envelope .wordmark { left: 16px; top: 26px; font-size: 22px; }
  .envelope .wordmark .dot { width: 22px; height: 22px; }
  .envelope .address { left: 18px; top: 63px; font-size: 8.5px; line-height: 11.6px; }
  .envelope .ghost-mark { left: -40px; top: 120px; width: 180px; height: 180px; }

  /* Business card */
  .business-card { left: 808px; top: 643px; width: 320px; height: 183px; }
  .business-card .band { height: 20px; }
  .business-card .wordmark { left: 177px; top: 20px; font-size: 22px; }
  .business-card .wordmark .dot { width: 22px; height: 22px; }
  .business-card .holder-name {
    position: absolute; left: 79px; top: 87px; margin: 0;
    font-size: 14px; font-weight: 600; color: var(--ink); letter-spacing: 0.2px;
  }
  .business-card .address { left: 177px; top: 112px; font-size: 8px; line-height: 11.3px; }
  .business-card .ghost-mark { left: -30px; top: 48px; width: 110px; height: 110px; }

  /* Piece labels */
  .piece-label {
    position: absolute; margin: 0;
    font-family: "Montserrat", "Helvetica Neue", sans-serif;
    font-weight: 600; font-size: 16.5px; color: var(--label); letter-spacing: 0.3px;
  }
  .label-letterhead { left: 60px; top: 930px; }
  .label-envelope { right: 32px; top: 586px; }
  .label-card { left: 899px; top: 844px; }
</style>
</head>
<body>
<main class="stage">

  <section class="sheet letterhead" aria-label="Letterhead">
    <svg class="ghost-mark" viewBox="0 0 100 100" aria-hidden="true">
      <circle cx="50" cy="50" r="48" fill="var(--ghost-blue)"/>
    </svg>
    <div class="wordmark"><span class="dot"></span>Verano</div>
    <p class="address">0000 Harbour View Way<br>Westhaven Lakeshire<br>P.O Box 0000, LK<br>Tel: (555) 0100-0000</p>
    <div class="band"></div>
  </section>

  <section class="sheet envelope" aria-label="Envelope">
    <svg class="ghost-mark" viewBox="0 0 100 100" aria-hidden="true">
      <circle cx="50" cy="50" r="48" fill="var(--ghost-blue)"/>
    </svg>
    <div class="wordmark"><span class="dot"></span>Verano</div>
    <p class="address">0000 Harbour View Way<br>Westhaven Lakeshire<br>P.O Box 0000, LK</p>
    <div class="band"></div>
  </section>

  <section class="sheet business-card" aria-label="Business card">
    <svg class="ghost-mark" viewBox="0 0 100 100" aria-hidden="true">
      <circle cx="50" cy="50" r="48" fill="var(--ghost-blue)"/>
    </svg>
    <div class="wordmark"><span class="dot"></span>Verano</div>
    <p class="holder-name">LENA MORETTI</p>
    <p class="address">0000 Harbour View Way<br>Westhaven Lakeshire<br>P.O Box 0000, LK<br>Tel: (555) 0100-0000</p>
    <div class="band"></div>
  </section>

  <p class="piece-label label-letterhead">LETTERHEAD</p>
  <p class="piece-label label-envelope">ENVELOPE</p>
  <p class="piece-label label-card">BUSINESS CARD</p>

</main>
</body>
</html>
```